Verdant Loop Advisors, LLC

I am looking for a simple, clear layout with my logo prominent and embossed, on the best quality card stock available. I would like the business name and phone number included on the card as well......I dont want my name anywhere on the card and I would like my logo embossed on the card......something simple with a white back......open to designs as long as they go along with recycling symbols and green type stuff.....The address, website, cell number, fax number, and email are listed below

5374 Tillbury Fenwood Road
Larkmoor, MD 20999

c. 240.555.0143 f. 240.555.0187
e. sales@verdantloopadvisors.example
w. www.verdantloopadvisors.example

Industry/Entity Type

Recycling

```html
<!DOCTYPE html>
<html lang="en">
<head>
<meta charset="utf-8">
<title>Verdant Loop Advisors, LLC – Business Card</title>
<link rel="stylesheet" href="https://fonts.googleapis.com/css2?family=Arvo&display=swap">
<style>
  :root {
    --card-green: #1f6a27;
    --frame-green: #2f7d35;
    --deep-green: #0f4a16;
    --ink-light: #f4f4f0;
  }
  * { box-sizing: border-box; margin: 0; padding: 0; }
  html, body {
    width: 1200px; height: 777px; overflow: hidden;
    background: var(--card-green);
  }
  .card {
    position: relative; width: 1200px; height: 777px;
    background: var(--card-green);
    font-family: "Arvo", "Rockwell", serif;
  }
  .card__frame {
    position: absolute; inset: 12px;
    border: 1px solid var(--frame-green);
  }
  .brand {
    position: absolute; left: 88px; top: 281px; width: 430px;
    display: flex; flex-direction: column; align-items: center;
  }
  .brand__mark {
    width: 122px; height: 122px; border-radius: 50%;
    background: var(--deep-green);
    margin-bottom: 24px;
  }
  .brand__name {
    color: var(--deep-green);
    font-size: 36px; line-height: 1.2; font-weight: 400;
    text-align: center; letter-spacing: 1px;
  }
  .divider {
    position: absolute; left: 601px; top: 209px;
    width: 2px; height: 359px; background: var(--deep-green);
  }
  .contact {
    position: absolute; left: 634px; top: 262px;
    list-style: none; color: var(--ink-light);
    font-size: 26px; line-height: 1.35;
  }
  .contact__row { display: flex; align-items: center; }
  .contact__row + .contact__row { margin-top: 24px; }
  .contact__row--address { align-items: flex-start; }
  .contact__address { font-style: normal; }
  .contact__icon {
    width: 40px; height: 40px; flex: none; margin-right: 16px;
    fill: var(--deep-green); stroke: none;
  }
  .contact__row--address .contact__icon { margin-top: 2px; }
  .contact__phone { display: flex; align-items: center; }
  .contact__phone + .contact__phone { margin-left: 32px; }
</style>
</head>
<body>
<main class="card">
  <div class="card__frame"></div>

  <section class="brand">
    <div class="brand__mark"></div>
    <h1 class="brand__name">Verdant Loop<br>Advisors, LLC</h1>
  </section>

  <div class="divider"></div>

  <ul class="contact">
    <li class="contact__row contact__row--address">
      <svg class="contact__icon" viewBox="0 0 40 40" aria-hidden="true">
        <path d="M20 3c-6.6 0-11 4.8-11 10.8C9 21.5 20 37 20 37s11-15.5 11-23.2C31 7.8 26.6 3 20 3zm0 15a4.4 4.4 0 1 1 0-8.8 4.4 4.4 0 0 1 0 8.8z"/>
      </svg>
      <address class="contact__address">5374 Tillbury Fenwood Road<br>Larkmoor, MD 20999</address>
    </li>
    <li class="contact__row">
      <span class="contact__phone">
        <svg class="contact__icon" viewBox="0 0 40 40" aria-hidden="true">
          <path d="M5 14c0-4 7-7 15-7s15 3 15 7v3h-7v-3c-2-1-5-1.5-8-1.5s-6 .5-8 1.5v3H5z"/>
          <path d="M11 19h18l4 13H7z"/>
        </svg>
        240.555.0143
      </span>
      <span class="contact__phone">
        <svg class="contact__icon" viewBox="0 0 40 40" aria-hidden="true">
          <path d="M10 4l6 7-3 4c2 5 6 9 11 11l4-3 7 6-4 6C18 35 5 22 4 9z"/>
        </svg>
        240.555.0187
      </span>
    </li>
    <li class="contact__row">
      <svg class="contact__icon" viewBox="0 0 40 40" aria-hidden="true">
        <path d="M3 9h34v22H3zm3 3v.5l14 10 14-10V12zm0 4v12h28V16L20 26z"/>
      </svg>
      sales@verdantloopadvisors.example
    </li>
    <li class="contact__row">
      <svg class="contact__icon" viewBox="0 0 40 40" aria-hidden="true">
        <circle cx="20" cy="20" r="17"/>
        <text x="20" y="24" text-anchor="middle" font-family="Arial, sans-serif" font-size="11" font-weight="700" fill="#1f6a27">www</text>
      </svg>
      www.verdantloopadvisors.example
    </li>
  </ul>
</main>
</body>
</html>
```